Presentation Folder - Stagger Cut Fliers
Keystone Realty Group
Presentation Folder - Stagger Cut Fliers - Real Estate
Creative Brief
Real Estate
Corporate. Our target audience are real estate agents and brokers. This is an industry where image and perception matter, so these designs need to invoke professionalism, be creative, and invoke confidence in our services.
The presentation folder itself needs to be very simple, but again, very professional and aesthetically pleasing. At a minimum, we need our logo on the font and the company contact information on the back. The stagger cut fliers themselves need to have the ability to put information on the front and back of the flier. There are five pages for the fliers, so you can either design five unique pages or have a template that can work for all of them. You can use filler text like that in the attached document. The fliers aren't just going to be text. You can add filler images to make more appealing, such as on the consumer demand page you can leave a spot where we can put the image of a billboard.

```html
<!DOCTYPE html>
<html lang="en">
<head>
<meta charset="utf-8">
<title>Keystone Realty Group – Stagger Cut Fliers</title>
<link href="https://fonts.googleapis.com/css2?family=PT+Sans:wght@400;700&display=swap" rel="stylesheet">
<style>
  :root{
    --board:#4a4a4a;
    --navy:#0b356f;
    --blue:#1d5ca8;
    --sky:#5d9bd8;
    --ice:#e6eef8;
    --paper:#ffffff;
    --ink:#4d4d4d;
    --photo-warm:#b99a78;
    --photo-green:#7f9c6a;
    --photo-sky:#a9c3dc;
  }
  html,body{margin:0;padding:0;overflow:hidden;}
  body{font-family:"PT Sans",Arial,sans-serif;}
  .canvas{position:relative;width:1200px;height:976px;background:var(--board);overflow:hidden;}

  .flyer{position:absolute;width:368px;height:436px;background:var(--paper);overflow:hidden;box-shadow:0 2px 6px rgba(0,0,0,.35);}
  .flyer-header{position:absolute;left:0;top:0;width:368px;height:78px;display:block;}
  .flyer-title{position:absolute;top:10px;margin:0;color:var(--paper);font-size:22px;font-weight:700;letter-spacing:.2px;}
  .flyer-footer{position:absolute;left:0;bottom:0;width:368px;height:60px;display:block;}

  .brand{position:absolute;bottom:10px;display:flex;align-items:center;gap:5px;background:var(--paper);padding:4px 8px;border-radius:12px;z-index:3;}
  .brand-dot{width:12px;height:12px;border-radius:50%;background:var(--blue);}
  .brand-name{font-size:10px;font-weight:700;color:var(--blue);}
  .brand.right{right:10px;}
  .brand.left{left:10px;}

  .label{display:inline-block;background:linear-gradient(90deg,var(--navy),var(--blue));color:var(--paper);font-size:9px;font-weight:700;padding:2px 24px 2px 6px;margin-bottom:3px;}
  .heading{margin:0 0 3px;font-size:10px;font-weight:700;color:var(--blue);}
  .copy{margin:0;font-size:6.5px;line-height:1.4;color:var(--ink);}

  .block{position:absolute;}
  .panel{position:absolute;background:var(--ice);border-left:3px solid var(--blue);padding:5px 7px;box-sizing:border-box;}

  .photo{position:absolute;box-sizing:border-box;}
  .framed{border:4px solid var(--paper);box-shadow:0 1px 4px rgba(0,0,0,.35);}

  .qr-box{position:absolute;background:var(--paper);border:2px solid #9aa5b3;box-sizing:border-box;}

  .affiliate-band{position:absolute;left:0;top:220px;width:368px;height:216px;background:linear-gradient(180deg,var(--blue),var(--navy));}
  .affiliate-band .heading{color:var(--paper);}
  .affiliate-band .copy{color:#dbe7f5;}
</style>
</head>
<body>
<div class="canvas">

  <!-- shared shapes -->
  <svg width="0" height="0" style="position:absolute">
    <defs>
      <linearGradient id="headGrad" x1="0" y1="0" x2="0" y2="1">
        <stop offset="0" stop-color="#0b356f"/>
        <stop offset="1" stop-color="#2a6fbf"/>
      </linearGradient>
      <linearGradient id="footGrad" x1="0" y1="0" x2="1" y2="0">
        <stop offset="0" stop-color="#0b356f"/>
        <stop offset="1" stop-color="#2a6fbf"/>
      </linearGradient>
      <symbol id="header-wave" viewBox="0 0 368 78" preserveAspectRatio="none">
        <rect width="368" height="78" fill="url(#headGrad)"/>
        <path d="M0 64 Q170 36 368 50" fill="none" stroke="#7fb2e6" stroke-width="3"/>
        <path d="M0 70 Q170 44 368 58 L368 78 L0 78 Z" fill="#ffffff"/>
      </symbol>
      <symbol id="footer-wave" viewBox="0 0 368 60" preserveAspectRatio="none">
        <path d="M0 14 Q150 58 368 18 L368 60 L0 60 Z" fill="url(#footGrad)"/>
        <path d="M0 8 Q150 52 368 12" fill="none" stroke="#7fb2e6" stroke-width="2.5"/>
      </symbol>
    </defs>
  </svg>

  <!-- Flyer 1: SignText Features -->
  <section class="flyer" style="left:26px;top:22px;">
    <svg class="flyer-header"><use href="#header-wave" width="368" height="78"/></svg>
    <h2 class="flyer-title" style="left:14px;">SignText Features</h2>
    <div class="block" style="left:12px;top:70px;width:344px;">
      <div class="label">Feature 1</div>
      <p class="copy">Each sign rider carries a short code that buyers text for instant photos, price and details of the listing, sent straight to their phone.</p>
    </div>
    <div class="block" style="left:12px;top:136px;width:344px;">
      <div class="label">Feature 2</div>
      <p class="copy">Every inquiry is captured and forwarded to the agent at once, so no buyer lead is lost and follow up can start the same day.</p>
    </div>
    <div class="block" style="left:12px;top:202px;width:344px;">
      <div class="label">Feature 3</div>
      <p class="copy">Each sign rider carries a short code that buyers text for instant photos, price and details of the listing, sent straight to their phone.</p>
    </div>
    <div class="block" style="left:12px;top:268px;width:344px;">
      <div class="label">Feature 4</div>
      <p class="copy">Every inquiry is captured and forwarded to the agent at once, so no buyer lead is lost and follow up can start the same day.</p>
    </div>
    <svg class="flyer-footer"><use href="#footer-wave" width="368" height="60"/></svg>
    <div class="photo" role="img" aria-label="Photo of a two-storey suburban house with a front lawn" style="left:110px;top:338px;width:188px;height:98px;background:linear-gradient(180deg,var(--photo-sky) 0%,#c9d6e2 45%,var(--photo-warm) 60%,var(--photo-green) 100%);z-index:2;"></div>
    <div class="qr-box" style="left:304px;top:350px;width:56px;height:78px;z-index:2;"></div>
    <div class="brand left"><span class="brand-dot"></span><span class="brand-name">Keystone Realty Group</span></div>
  </section>

  <!-- Flyer 2: Consumer Demand -->
  <section class="flyer" style="left:416px;top:22px;">
    <svg class="flyer-header"><use href="#header-wave" width="368" height="78"/></svg>
    <h2 class="flyer-title" style="left:60px;">Consumer Demand</h2>
    <div class="panel" style="left:10px;top:76px;width:172px;height:76px;">
      <h3 class="heading">Technique 1</h3>
      <p class="copy">Buyers now search from the street. Signs, billboards and print ads that invite a quick text turn passing interest into real contacts.</p>
    </div>
    <div class="photo framed" role="img" aria-label="Billboard space for a roadside advertisement" style="left:190px;top:72px;width:166px;height:86px;background:linear-gradient(180deg,#dfe8f2,#9fb8d2);"></div>
    <div class="photo framed" role="img" aria-label="Photo of a studio microphone" style="left:10px;top:164px;width:122px;height:74px;background:linear-gradient(135deg,#8a2a2a,#d9b9a6);"></div>
    <div class="panel" style="left:140px;top:166px;width:216px;height:70px;">
      <h3 class="heading">Technique 2</h3>
      <p class="copy">Buyers now search from the street. Signs, billboards and print ads that invite a quick text turn passing interest into real contacts.</p>
    </div>
    <div class="panel" style="left:10px;top:246px;width:172px;height:72px;">
      <h3 class="heading">Technique 3</h3>
      <p class="copy">Buyers now search from the street. Signs, billboards and print ads that invite a quick text turn passing interest into real contacts.</p>
    </div>
    <div class="photo framed" role="img" aria-label="Photo of a person reading a newspaper ad" style="left:190px;top:244px;width:166px;height:76px;background:linear-gradient(135deg,#c6a98c,#eadfd2);"></div>
    <div class="photo framed" role="img" aria-label="Screenshot of a mobile listing page" style="left:10px;top:328px;width:128px;height:70px;background:linear-gradient(180deg,#3a6fb0,#e8eef6);z-index:2;"></div>
    <div class="panel" style="left:146px;top:328px;width:210px;height:58px;z-index:2;">
      <h3 class="heading">Technique 4</h3>
      <p class="copy">Buyers now search from the street. Signs, billboards and print ads that invite a quick text turn passing interest into real contacts.</p>
    </div>
    <svg class="flyer-footer"><use href="#footer-wave" width="368" height="60"/></svg>
    <div class="brand right"><span class="brand-dot"></span><span class="brand-name">Keystone Realty Group</span></div>
  </section>

  <!-- Flyer 3: Lead Generation -->
  <section class="flyer" style="left:806px;top:22px;">
    <svg class="flyer-header"><use href="#header-wave" width="368" height="78"/></svg>
    <h2 class="flyer-title" style="left:110px;">Lead Generation</h2>
    <div class="block" style="left:12px;top:80px;width:170px;">
      <h3 class="heading">Technique 1</h3>
      <p class="copy">Every inquiry is captured and forwarded to the agent at once, so no buyer lead is lost and follow up can start the same day.</p>
    </div>
    <div class="block" style="left:12px;top:180px;width:170px;">
      <h3 class="heading">Technique 2</h3>
      <p class="copy">Each sign rider carries a short code that buyers text for instant photos, price and details of the listing, sent straight to their phone.</p>
    </div>
    <div class="block" style="left:12px;top:282px;width:170px;">
      <h3 class="heading">Technique 3</h3>
      <p class="copy">Every inquiry is captured and forwarded to the agent at once, so no buyer lead is lost and follow up can start the same day.</p>
    </div>
    <div class="photo framed" role="img" aria-label="Photo of a smiling family outdoors" style="left:196px;top:60px;width:160px;height:92px;background:linear-gradient(180deg,var(--photo-sky),#e2d6c6);transform:rotate(3deg);"></div>
    <div class="photo framed" role="img" aria-label="Photo of a brick family home" style="left:192px;top:168px;width:160px;height:92px;background:linear-gradient(180deg,var(--photo-sky) 0%,#a57c5e 55%,var(--photo-green) 100%);transform:rotate(-2deg);"></div>
    <div class="photo framed" role="img" aria-label="Photo of a family sitting on the lawn" style="left:196px;top:276px;width:160px;height:92px;background:linear-gradient(180deg,#c2d3e4,var(--photo-green));transform:rotate(2deg);z-index:2;"></div>
    <svg class="flyer-footer"><use href="#footer-wave" width="368" height="60"/></svg>
    <div class="brand right"><span class="brand-dot"></span><span class="brand-name">Keystone Realty Group</span></div>
  </section>

  <!-- Flyer 4: Return on Investment -->
  <section class="flyer" style="left:210px;top:528px;">
    <svg class="flyer-header"><use href="#header-wave" width="368" height="78"/></svg>
    <h2 class="flyer-title" style="left:84px;">Return on Investment</h2>
    <div class="photo" role="img" aria-label="Illustration of a rising 3D bar chart with growth arrows" style="left:14px;top:96px;width:160px;height:236px;background:radial-gradient(ellipse at 50% 60%,#d8e6c8 0%,#eef3f8 70%,var(--paper) 100%);"></div>
    <div class="block" style="left:184px;top:160px;width:172px;">
      <div class="label">Technique 1</div>
      <p class="copy">Buyers now search from the street. Signs, billboards and print ads that invite a quick text turn passing interest into real contacts.</p>
    </div>
    <div class="block" style="left:184px;top:244px;width:172px;">
      <div class="label">Technique 2</div>
      <p class="copy">Each sign rider carries a short code that buyers text for instant photos, price and details of the listing, sent straight to their phone.</p>
    </div>
    <svg class="flyer-footer"><use href="#footer-wave" width="368" height="60"/></svg>
    <div class="brand right"><span class="brand-dot"></span><span class="brand-name">Keystone Realty Group</span></div>
  </section>

  <!-- Flyer 5: Broker Affiliate Program -->
  <section class="flyer" style="left:608px;top:528px;">
    <svg class="flyer-header"><use href="#header-wave" width="368" height="78"/></svg>
    <h2 class="flyer-title" style="left:64px;">Broker Affiliate Program</h2>
    <div class="photo" role="img" aria-label="Photo of a business handshake" style="left:0;top:58px;width:368px;height:164px;background:linear-gradient(90deg,#2c3540 0%,#c49a7c 45%,#d9b79a 55%,#3a4350 100%);"></div>
    <div class="affiliate-band">
      <div class="block" style="left:12px;top:18px;width:164px;">
        <h3 class="heading">Technique 1</h3>
        <p class="copy">Every inquiry is captured and forwarded to the agent at once, so no buyer lead is lost and follow up can start the same day.</p>
      </div>
      <div class="block" style="left:192px;top:18px;width:164px;">
        <h3 class="heading">Technique 2</h3>
        <p class="copy">Buyers now search from the street. Signs, billboards and print ads that invite a quick text turn passing interest into real contacts.</p>
      </div>
    </div>
    <svg class="flyer-footer" viewBox="0 0 368 60" preserveAspectRatio="none">
      <path d="M150 60 Q270 30 368 22 L368 60 Z" fill="#ffffff"/>
      <path d="M150 58 Q270 28 368 18" fill="none" stroke="#7fb2e6" stroke-width="2.5"/>
    </svg>
    <div class="brand right"><span class="brand-dot"></span><span class="brand-name">Keystone Realty Group</span></div>
  </section>

</div>
</body>
</html>
```